"Quiet Lanterns Burning" cat novel book cover

Cover for a novel about a vet tech who saves two kittens from euthanization and ends up entangled in an adventure she never could have dreamed.

Novel has four point-of-view characters: a female vet tech protagonist, a one-eyed kitten who she saves and adopts, a male pastor who befriends the vet tech after finding said kitten hiding under his porch, and a pharmaceutical executive antagonist in charge of a dubious feline weight-loss drug.

The two kittens saved by the protagonist also fall in love about 1/4 of the way through the story. One of them has a CNS condition that makes it hard for them to walk, and the point-of-view cat serves as a protector and defender of the disabled one.

Narrative has a lot of focus on the emotional lives of the characters and their relationships, but it is not a romance novel per se. While the title is a Biblical reference and religion and spirituality are important to some of the characters, it is also not meant to support any particular belief system.

Target Market(s)

Cat lovers

Requirements
Must have
• Title: Quiet Lanterns Burning
Author: Delia Brackenford
Tagline (to appear on cover): Even the smallest kitty can change the world
Nice to have
• I originally intended to use the attached photo representing the story's central kittens. I was going to apply some filters to make it look hand-drawn and disguise the low resolution. I quickly realized my graphic design skills are not sufficient to make that look professional, which led me here. If you can make it work with that photo, it would be lovely; if not, I am totally open to alternative concepts.
Should not have
• The appearances and even the ages of the characters are not solidified in the text, in order to allow the reader to imagine them any way they prefer. So I would prefer avoiding any specific visual representations of them, outside of something vague like a silhouette.

```html
<!DOCTYPE html>
<html lang="en">
<head>
<meta charset="utf-8">
<title>Quiet Lanterns Burning — Cover</title>
<link rel="stylesheet" href="https://fonts.googleapis.com/css2?family=Parisienne&family=Kalam:wght@700&family=Raleway:wght@400&display=swap">
<style>
  :root {
    --stage: #eeeeee;
    --cover-top: #d3a86a;
    --cover-mid: #f1c9a0;
    --cover-bottom: #fb8c70;
    --glow: #fffaf0;
    --title-purple: #5a1a85;
    --cat-purple: #4d136f;
    --ribbon-tan: #ecd2a6;
    --tagline-ink: #1b1414;
    --author-ink: #3a1a55;
  }
  * { margin: 0; padding: 0; box-sizing: border-box; }
  html, body {
    width: 1200px;
    height: 800px;
    overflow: hidden;
    background: var(--stage);
  }
  .canvas {
    position: relative;
    width: 1200px;
    height: 800px;
    display: flex;
    align-items: center;
    justify-content: center;
  }
  .cover {
    position: relative;
    width: 480px;
    height: 720px;
    overflow: hidden;
    background:
      radial-gradient(ellipse 260px 230px at 52% 22%, var(--glow) 0%, rgba(255,250,240,0.55) 40%, rgba(255,250,240,0) 100%),
      linear-gradient(180deg, var(--cover-top) 0%, var(--cover-mid) 38%, #f6a982 68%, var(--cover-bottom) 100%);
  }
  .title {
    position: absolute;
    inset: 0;
    font-family: "Parisienne", cursive;
    color: var(--title-purple);
    font-weight: 400;
    line-height: 1;
  }
  .title span {
    position: absolute;
    white-space: nowrap;
  }
  .title-quiet {
    left: 92px;
    top: 30px;
    font-size: 62px;
    transform: rotate(-6deg);
  }
  .title-lanterns {
    left: 48px;
    top: 100px;
    font-size: 92px;
    transform: rotate(-5deg);
  }
  .title-burning {
    left: 180px;
    top: 205px;
    font-size: 88px;
    transform: rotate(-3deg);
  }
  .artwork {
    position: absolute;
    left: 105px;
    top: 313px;
    width: 317px;
    height: 341px;
    border-radius: 40px;
    background: linear-gradient(180deg, rgba(77,19,111,0.85) 0%, rgba(77,19,111,0.55) 32%, rgba(236,210,166,0.9) 48%, rgba(236,210,166,0.8) 85%, rgba(236,210,166,0) 100%);
  }
  .tagline {
    position: absolute;
    font-family: "Kalam", cursive;
    font-weight: 700;
    color: var(--tagline-ink);
    white-space: nowrap;
    font-size: 27px;
    line-height: 1;
  }
  .tagline-first {
    left: 122px;
    top: 468px;
    transform: rotate(9deg);
    transform-origin: left center;
  }
  .tagline-second {
    left: 158px;
    top: 538px;
    transform: rotate(7deg);
    transform-origin: left center;
  }
  .author {
    position: absolute;
    left: 0;
    right: 0;
    top: 664px;
    text-align: center;
    font-family: "Raleway", sans-serif;
    font-weight: 400;
    font-size: 23px;
    color: var(--author-ink);
    letter-spacing: 0.2px;
  }
</style>
</head>
<body>
  <main class="canvas">
    <article class="cover">
      <h1 class="title">
        <span class="title-quiet">Quiet</span>
        <span class="title-lanterns">Lanterns</span>
        <span class="title-burning">Burning</span>
      </h1>
      <div class="artwork" role="img" aria-label="Illustration: two purple cat silhouettes sitting nose to nose on a curling tan ribbon banner"></div>
      <p class="tagline tagline-first">Even the smallest kitty</p>
      <p class="tagline tagline-second">can change the world</p>
      <p class="author">Delia Brackenford</p>
    </article>
  </main>
</body>
</html>
```